New Business Card Design Project

We are looking for a talented individual to create a truly awesome/unique business card design for us. We are looking for a someone to design something that will really stand out from the crowd - we don't mind what ideas you come up with (ie embossed/flat/matte/shine etc etc) just wow us with your creativity.
Updates

Target Market(s)

Video Games Industry Professionals (all levels of seniority from QA Testers through to CEOs)

Contact Information for Business Card

Company logo (see upload)
Company name: Northbay Play Careers Ltd
Employee Name: Darren Elsby
Job title: CEO
Website: www.nbpc2go.example
Office +44 1632 960418
Mobile: +44 7700 900276
Email: darren@nbpc2go.example

Colors

Designer to choose colors to be used in the design.

Requirements
Must have
• The business card design MUST contain all the information listed in the BUSINESS CARD DETAILS box.
• You will see the colours that are relevant to us (ie company logo) in the uploaded imagery - however you do not have to use all these colours when designing the business card itself
• MUST BE DOUBLE SIDED

```html
<!DOCTYPE html>
<html lang="en">
<head>
<meta charset="utf-8">
<title>Northbay Play Careers – Business Card</title>
<link rel="stylesheet" href="https://fonts.googleapis.com/css2?family=Nunito:wght@300;400;800;900&display=swap">
<style>
  :root {
    --stage: #7b7b7b;
    --navy-deep: #1c1c30;
    --navy: #2f2f4c;
    --orange: #ef871c;
    --orange-dark: #c4661a;
    --peach: #f6b77a;
    --lemon: #f1ee7c;
    --lilac: #a9a6e0;
    --violet: #b98fe0;
    --pink: #f49cd6;
    --white: #ffffff;
  }
  * { box-sizing: border-box; margin: 0; padding: 0; }
  html, body { width: 1200px; height: 1200px; overflow: hidden; }
  body {
    background: var(--stage);
    font-family: "Nunito", Arial, sans-serif;
    position: relative;
  }
  .card {
    position: absolute;
    left: 198px;
    width: 804px;
    height: 520px;
    border-radius: 22px;
    overflow: hidden;
  }
  .card--front { top: 40px; }
  .card--back {
    top: 639px;
    background: linear-gradient(90deg, var(--navy) 0%, var(--navy-deep) 100%);
  }
  .card__shape { position: absolute; inset: 0; }

  .mascot-art {
    position: absolute;
    background: radial-gradient(ellipse at 65% 80%, var(--pink) 0%, var(--violet) 45%, var(--lilac) 80%, rgba(169,166,224,0) 100%);
    opacity: .9;
  }
  .card--front .mascot-art {
    left: 74px; top: 40px; width: 248px; height: 196px;
    border-radius: 45% 50% 45% 40%;
  }
  .card--back .mascot-art {
    left: 0; top: 24px; width: 406px; height: 496px;
    border-radius: 0 55% 45% 0;
  }

  .holder {
    position: absolute; left: 69px; top: 246px; color: var(--white);
  }
  .holder__marker {
    position: absolute; left: 58px; top: 252px;
    width: 0; height: 0;
    border-top: 26px solid transparent;
    border-bottom: 26px solid transparent;
    border-left: 24px solid var(--orange);
  }
  .holder__title {
    font-weight: 300; font-size: 44px; line-height: 40px; letter-spacing: -1px;
  }
  .holder__name {
    font-weight: 900; font-size: 42px; line-height: 48px; letter-spacing: -0.5px;
  }
  .contact {
    position: absolute; left: 69px; top: 329px;
    list-style: none; color: var(--white);
    font-size: 18px; line-height: 21px; font-weight: 300; letter-spacing: 0.6px;
  }
  .contact li:last-child { font-weight: 400; letter-spacing: 0; }
  .web {
    position: absolute; color: var(--white); font-size: 17px; font-weight: 400;
  }
  .card--front .web { left: 58px; top: 458px; }

  .dot {
    position: absolute; width: 28px; height: 28px; border-radius: 50%; top: 246px;
  }
  .dot--orange { left: 340px; background: var(--orange); }
  .dot--navy { left: 432px; background: var(--navy); }

  .brand-name--vertical {
    position: absolute; left: 620px; top: 260px;
    transform: translate(-50%, -50%) rotate(-90deg);
    white-space: nowrap;
    color: var(--navy);
    font-weight: 900; font-size: 44px; line-height: 44px; text-align: center;
  }

  .stripe { position: absolute; left: 0; top: 43px; width: 804px; height: 13px; display: flex; }
  .stripe span { height: 100%; }
  .stripe .s-orange { background: var(--orange); }
  .stripe .s-peach { background: var(--peach); }
  .stripe .s-lemon { background: var(--lemon); }

  .brand-tile {
    position: absolute; left: 546px; top: 214px; width: 170px; height: 100px;
    border-radius: 12px;
    background: linear-gradient(135deg, #8fd0d6 0%, #b7b3e6 35%, #c28ae0 60%, #e8b0d8 80%, #c9c6cf 100%);
    display: flex; align-items: center; justify-content: center; text-align: center;
    color: var(--navy); font-weight: 900; font-size: 17px; line-height: 19px;
  }
  .pointer-bar {
    position: absolute; left: 730px; top: 222px; width: 7px; height: 84px; background: var(--orange);
  }
  .pointer {
    position: absolute; left: 747px; top: 222px; width: 0; height: 0;
    border-top: 42px solid transparent; border-bottom: 42px solid transparent;
    border-left: 40px solid var(--orange);
  }
  .card--back .web { left: 632px; top: 324px; transform: translateX(-50%); white-space: nowrap; }
</style>
</head>
<body>

  <section class="card card--front" aria-label="Card front">
    <svg class="card__shape" width="804" height="520" viewBox="0 0 804 520" aria-hidden="true">
      <defs>
        <linearGradient id="navyPanel" x1="0" x2="1" y1="0" y2="0">
          <stop offset="0" stop-color="#1e1e32"/>
          <stop offset="1" stop-color="#30304d"/>
        </linearGradient>
        <linearGradient id="pocketShade" x1="0" x2="1" y1="0" y2="0">
          <stop offset="0" stop-color="#b7601a"/>
          <stop offset="0.18" stop-color="#ef871c"/>
          <stop offset="1" stop-color="#ef871c"/>
        </linearGradient>
      </defs>
      <rect x="440" y="0" width="364" height="520" fill="url(#pocketShade)"/>
      <rect x="458" y="14" width="328" height="490" rx="14" fill="none" stroke="#b9621d" stroke-width="1.5"/>
      <path d="M0 0 H452 V36 Q452 64 424 66 Q406 68 406 90 V432 Q406 452 424 454 Q452 458 452 486 V520 H0 Z" fill="url(#navyPanel)"/>
      <rect x="400" y="86" width="5" height="350" fill="#14141f"/>
      <rect x="781" y="276" width="8" height="28" fill="#2f2f4c"/>
      <rect x="781" y="324" width="8" height="30" fill="#9a9aa6"/>
      <rect x="781" y="354" width="8" height="6" fill="#ffffff"/>
      <rect x="781" y="360" width="8" height="116" fill="#1e1e32"/>
      <rect x="781" y="496" width="8" height="8" fill="#2f2f4c"/>
    </svg>

    <div class="mascot-art" role="img" aria-label="Horned-helmet warrior mascot illustration in lilac-to-pink gradient"></div>

    <span class="holder__marker" aria-hidden="true"></span>
    <div class="holder">
      <p class="holder__title">CEO</p>
      <p class="holder__name">Darren Elsby</p>
    </div>
    <ul class="contact">
      <li>Office+44 1632 960418</li>
      <li>Mobile:+44 7700 900276</li>
      <li>Email:darren@nbpc2go.example</li>
    </ul>
    <p class="web">www.nbpc2go.example</p>

    <span class="dot dot--orange" aria-hidden="true"></span>
    <span class="dot dot--navy" aria-hidden="true"></span>

    <p class="brand-name--vertical">Northbay Play<br>Careers</p>
  </section>

  <section class="card card--back" aria-label="Card back">
    <div class="stripe" aria-hidden="true">
      <span class="s-orange" style="width:74px"></span>
      <span class="s-peach" style="width:91px"></span>
      <span class="s-lemon" style="width:474px"></span>
      <span class="s-peach" style="width:91px"></span>
      <span class="s-orange" style="width:74px"></span>
    </div>

    <div class="mascot-art" role="img" aria-label="Large horned-helmet warrior mascot illustration in lilac-to-pink gradient"></div>

    <div class="brand-tile">Northbay Play<br>Careers</div>
    <span class="pointer-bar" aria-hidden="true"></span>
    <span class="pointer" aria-hidden="true"></span>
    <p class="web">www.nbpc2go.example</p>
  </section>

</body>
</html>
```